I want to revise my business card design and get a more modern and up to date design.

Brolvane Handyman Sevices originated from a family-owned and operated contractor business, performing home renovation, addition, and construction work in the NYC area since 2004. Today, we specialize in reliable and affordable handyman services for residential and commercial clients In 2014, we expanded to northern New Jersey. In 2016, we brought quality home improvement and repair services to new Bucks County, PA, and nearby New Jersey areas.
Target Market(s)
Home owners and business that might be looking for a General contractor, handyman, cleaning services and Home maintenance and property.
Industry/Entity Type
Construction Company
Contact Information for Business Card
I am open to new ideas
Colors
Designer to choose colors to be used in the design.
Look and feel
Each slider illustrates characteristics of the customer's brand and the style your logo design should communicate.

```html
<!DOCTYPE html>
<html lang="en">
<head>
<meta charset="UTF-8">
<title>Brolvane Handyman Sevices – Business Card</title>
<link href="https://fonts.googleapis.com/css2?family=Montserrat:wght@400;500;700;800&display=swap" rel="stylesheet">
<style>
  :root {
    --bg: #3b3b3d;
    --card: #ffffff;
    --ink: #121212;
    --muted: #5a5a5a;
    --red: #e5202a;
    --faint: #f2f2f2;
    --badge: #e4e4e6;
  }
  * { margin: 0; padding: 0; box-sizing: border-box; }
  html, body { width: 1200px; height: 1000px; overflow: hidden; }
  body { background: var(--bg); font-family: "Montserrat", sans-serif; position: relative; }

  .card {
    position: absolute; left: 210px; width: 780px; height: 446px;
    background: var(--card); border-radius: 26px; overflow: hidden;
  }
  .card--front { top: 36px; }
  .card--back { top: 518px; }

  .brand { position: absolute; display: flex; align-items: flex-start; }
  .brand__mark { background: var(--red); flex: none; }
  .brand__text { display: flex; flex-direction: column; }
  .brand__name { font-weight: 800; color: var(--ink); line-height: 1; letter-spacing: -1px; white-space: nowrap; }
  .brand__tag { font-weight: 500; color: var(--muted); text-transform: uppercase; white-space: nowrap; }

  .card--front .brand { left: 150px; top: 92px; gap: 26px; }
  .card--front .brand__mark { width: 120px; height: 120px; }
  .card--front .brand__name { font-size: 84px; }
  .card--front .brand__tag { font-size: 20px; letter-spacing: 7px; margin-top: 12px; margin-left: 4px; }

  .partners { position: absolute; left: 150px; top: 300px; display: flex; gap: 30px; }
  .partners__badge { width: 150px; height: 40px; border-radius: 8px; background: var(--badge); }

  .watermark {
    position: absolute; left: 30px; top: 28px; width: 320px; height: 370px;
    background: var(--faint); border-radius: 40px;
  }
  .contact { position: absolute; left: 0; top: 250px; }
  .contact__bar { position: absolute; left: 0; top: 0; width: 22px; height: 100px; background: var(--red); }
  .contact__body { position: absolute; left: 58px; top: 6px; white-space: nowrap; }
  .contact__name { font-size: 22px; font-weight: 700; color: var(--red); letter-spacing: 1px; text-transform: uppercase; margin-bottom: 8px; }
  .contact__line { display: flex; align-items: center; gap: 8px; font-size: 15px; color: var(--ink); line-height: 1.5; }
  .contact__line svg { width: 12px; height: 12px; fill: var(--red); flex: none; }

  .card--back .brand { left: 372px; top: 92px; gap: 16px; }
  .card--back .brand__mark { width: 80px; height: 80px; }
  .card--back .brand__name { font-size: 54px; }
  .card--back .brand__tag { font-size: 13px; letter-spacing: 4.5px; margin-top: 9px; margin-left: 3px; }

  .services { position: absolute; right: 40px; top: 312px; text-align: right; }
  .services__line { font-size: 15px; font-weight: 700; color: var(--ink); line-height: 1.4; }
  .services__actions { font-size: 16px; font-weight: 700; color: var(--red); margin-top: 6px; letter-spacing: 0.5px; }
</style>
</head>
<body>

<section class="card card--front">
  <div class="brand">
    <div class="brand__mark" aria-hidden="true"></div>
    <div class="brand__text">
      <span class="brand__name">Brolvane</span>
      <span class="brand__tag">Handyman Services</span>
    </div>
  </div>
  <div class="partners" role="img" aria-label="Partner listing badges">
    <span class="partners__badge"></span>
    <span class="partners__badge"></span>
    <span class="partners__badge"></span>
  </div>
</section>

<section class="card card--back">
  <div class="watermark" role="img" aria-label="Faint large brand emblem decoration"></div>

  <div class="contact">
    <span class="contact__bar"></span>
    <div class="contact__body">
      <p class="contact__name">Marcus Delvane</p>
      <p class="contact__line">
        <svg viewBox="0 0 24 24"><path d="M6.6 10.8a15.1 15.1 0 0 0 6.6 6.6l2.2-2.2c.3-.3.7-.4 1-.2 1.1.4 2.3.6 3.6.6.6 0 1 .4 1 1V20c0 .6-.4 1-1 1A17 17 0 0 1 3 4c0-.6.4-1 1-1h3.5c.6 0 1 .4 1 1 0 1.3.2 2.5.6 3.6.1.3 0 .7-.2 1z"/></svg>
        (215) 555 -0147
      </p>
      <p class="contact__line">
        <svg viewBox="0 0 24 24"><path d="M2 5h20v14H2zm2 2v.5l8 5 8-5V7zm0 2.8V17h16V9.8l-8 5z"/></svg>
        brolvanehandyman@example.com
      </p>
    </div>
  </div>

  <div class="brand">
    <div class="brand__mark" aria-hidden="true"></div>
    <div class="brand__text">
      <span class="brand__name">Brolvane</span>
      <span class="brand__tag">Handyman Services</span>
    </div>
  </div>

  <div class="services">
    <p class="services__line">Commercial and Residential</p>
    <p class="services__line">Contractor | Handyman | Technician</p>
    <p class="services__actions">REPAIR | IMPROVE | MAINTAIN | REMODEL</p>
  </div>
</section>

</body>
</html>
```